Website for the K7VANT-Lab research laboratory.

We are a research team working on personality disorders. We would like a website that presents the team members (noting that students change frequently), ongoing projects with active recruitments, the latest publications, student resources, and possibly patient resources.

We have already prepared the logo with Plumvetta.

Our research areas:
1- Lifestyle Medicine and BPD
This area focuses on understanding lifestyle habits and their impact on the health of individuals living with Borderline Personality Disorder (BPD). It aims to improve essential components such as sleep, physical activity, and nutrition by identifying and promoting favorable lifestyle habits. The goal is to strengthen emotional regulation and improve overall health by fully integrating the physical dimension into recovery.
2- Interventions Supporting Psychosocial Functioning
Develop the full recovery potential and enhance social and professional integration strategies to support the life journey of patients in all its dimensions. This area focuses on practices and interventions that facilitate a return to an active life and harmonious integration into society.
3- Optimization of Psychotherapeutic Strategies in BPD
Optimize psychotherapeutic approaches for BPD by identifying the most effective methods, adapting them to individual needs, and evaluating their long-term impact. This research area aims to refine and personalize treatments to maximize their therapeutic benefits.
4- Biological Treatments for BPD: Neuromodulation and Pharmacotherapy
Develop and evaluate biological treatments, particularly in neuromodulation and pharmacotherapy, to improve the management of BPD. This area aims to explore scientific advances in these fields to offer complementary and innovative therapeutic options.

Vision
Affiliated with TVOLBAE, our laboratory is dedicated to creating tomorrow's interventions to offer a hopeful future for individuals living with Borderline Personality Disorder. We design and develop innovative solutions that integrate and value each individual, their loved ones, and their community, supporting their personal, social, functional, and physical recovery.

Values

Innovation
Our commitment to innovation guides every step of our research and development. We continually strive to push the boundaries of knowledge and techniques to create new and bold therapeutic solutions tailored to the evolving needs of individuals living with Borderline Personality Disorder.
Hope
We carry the hope of making a real difference in the lives of people living with BPD. This hope drives our work, pushing us to explore therapeutic approaches that offer patients a better and more serene future. By integrating this hope into our research, we are committed to developing interventions that inspire and support the recovery process. Through our research work, we wish to instill and spread hope.
Empathy and Personalization
We believe in a person-centered and inclusive approach where each individual is considered in their uniqueness and with compassion. By actively integrating patients and their experiences into our research, we aim to design solutions that not only meet their specific needs but also value their recovery while respecting their values. We wish to improve the satisfaction of individuals within the care network, promote the integration of their loved ones and their community.

```html
<!DOCTYPE html>
<html lang="en">
<head>
<meta charset="utf-8">
<title>K7VANT-Lab — BPD Research</title>
<link href="https://fonts.googleapis.com/css2?family=Tinos:wght@400;700&family=Poppins:wght@400;500;600;700&display=swap" rel="stylesheet">
<style>
:root{
  --teal:#12a195;
  --teal-dark:#0c7f76;
  --teal-soft:#3fb8ad;
  --orange:#ef7b1c;
  --ink:#1f2426;
  --muted:#6b7275;
  --bg:#f3f4f5;
  --white:#ffffff;
  --dark:#2a2d2f;
  --line:#dfe3e4;
}
*{box-sizing:border-box;margin:0;padding:0}
html,body{width:1200px;height:5372px;overflow:hidden}
body{position:relative;background:var(--bg);font-family:"Poppins",Arial,sans-serif;color:var(--ink);font-size:13px}
.abs{position:absolute}
.photo{position:absolute}
.btn{display:inline-block;background:var(--orange);color:#fff;font-weight:600;font-size:13px;padding:11px 28px;border-radius:4px}
.eyebrow{font-size:10px;font-weight:600;color:var(--orange);letter-spacing:.5px;display:flex;align-items:center;gap:10px}
.eyebrow::after{content:"";width:56px;height:2px;background:var(--orange)}
.eyebrow.center{justify-content:center}
.eyebrow.center::before{content:"";width:56px;height:2px;background:var(--orange)}
.section-title{font-family:"Tinos","Times New Roman",serif;font-weight:700;color:var(--teal);font-size:44px}
.copy{color:var(--muted);font-size:13px;line-height:1.6}

/* header */
.header{left:0;top:0;width:1200px;height:88px;background:var(--white)}
.topline{left:0;top:0;width:852px;height:36px;border-bottom:1px solid var(--line)}
.welcome{left:336px;top:10px;font-size:11px;font-weight:600;letter-spacing:.5px}
.mail{left:620px;top:9px;font-size:11px;display:flex;align-items:center;gap:8px}
.mail i{width:22px;height:16px;background:var(--teal);border-radius:3px;display:block}
.logo{display:flex;align-items:center;gap:10px;font-weight:700;color:var(--teal);font-size:20px}
.logo b{width:24px;height:24px;border-radius:50%;background:var(--teal);display:block}
.nav{left:330px;top:50px;display:flex;gap:40px;font-size:12px;font-weight:500}
.nav span.active{color:var(--teal);border-bottom:2px solid var(--teal);padding-bottom:4px}
.callbox{left:852px;top:0;width:348px;height:88px;background:var(--teal);color:#fff;display:flex;align-items:center;gap:16px;padding-left:28px}
.callbox .ic{width:44px;height:44px;border-radius:50%;background:#fff;display:flex;align-items:center;justify-content:center}
.callbox small{display:block;font-size:13px}
.callbox strong{font-size:22px;font-weight:700}

/* hero */
.hero-photo{left:0;top:88px;width:1200px;height:772px;background:linear-gradient(135deg,#5e5a55 0%,#8a857c 35%,#b3aea5 55%,#6e6a64 100%)}
.hero-card{left:80px;top:272px;width:468px;height:360px;background:#fff;border-left:8px solid var(--orange);padding:38px 40px}
.hero-card h1{font-family:"Tinos","Times New Roman",serif;font-weight:700;font-size:80px;line-height:.95;color:var(--teal)}
.hero-card p{margin:18px 0 22px;font-size:11px;color:var(--muted);line-height:1.6;width:380px}
.wave{left:0;top:740px}

/* mission */
.mission-art{left:132px;top:960px;width:428px;height:428px;border-radius:50%;background:linear-gradient(160deg,#8fcabf 0%,#3f9f95 50%,#2b6f86 100%)}
.mission{left:620px;top:995px;width:480px}
.mission h2{margin:14px 0 16px;line-height:1.1}

/* values */
.values{left:88px;top:1520px;width:1012px;height:228px;background:#fff;border-radius:0 0 60px 0;display:flex;padding:34px 48px;gap:40px;box-shadow:0 6px 20px rgba(0,0,0,.04)}
.value{flex:1;display:flex;gap:16px}
.value .ic{flex:none;width:52px;height:52px;border-radius:50%;border:2px solid var(--teal);display:flex;align-items:center;justify-content:center}
.value h3{font-family:"Tinos",serif;color:var(--teal);font-size:22px;line-height:1}
.value h4{color:var(--orange);font-size:12px;font-weight:600;margin:4px 0 8px}
.value p{font-size:11px;color:var(--muted);line-height:1.5}

/* services */
.arrows{left:1008px;top:1876px;display:flex;gap:12px}
.arrows span{width:44px;height:44px;background:#fff;display:flex;align-items:center;justify-content:center;border-radius:4px}
.arrows span.on{background:var(--dark)}
.svc{top:1972px;width:320px;height:390px}
.svc .photo{left:0;top:0;width:320px;height:200px}
.svc .box{position:absolute;left:36px;top:176px;width:284px;height:212px;background:#fff;padding:24px 26px;box-shadow:0 6px 18px rgba(0,0,0,.06)}
.svc .box h3{font-family:"Tinos",serif;font-size:20px;line-height:1.1;color:var(--teal);margin-bottom:10px}
.svc .box p{font-size:11px;color:var(--muted);line-height:1.5}
.svc .box a{display:block;margin-top:12px;color:var(--orange);font-weight:600;font-size:12px}
.svc.alt .box{background:var(--orange)}
.svc.alt .box h3,.svc.alt .box p,.svc.alt .box a{color:#fff}
.outline-btn{left:512px;top:2392px;width:168px;height:44px;border:1.5px solid var(--teal);border-radius:4px;color:var(--teal);font-weight:600;font-size:12px;display:flex;align-items:center;justify-content:center}

/* projects */
.projects-band{left:0;top:2520px;width:1200px;height:640px;background:#eceeef}
.proj-side{top:2692px;height:408px;border-radius:10px}
.proj-main{left:220px;top:2692px;width:756px;height:408px;border-radius:10px;background:linear-gradient(120deg,#c9c6bf,#a6a196 50%,#8d8a83)}
.proj-caption{left:256px;top:2868px;width:676px;height:80px;background:#fff;display:flex;align-items:center;padding-left:36px;font-weight:700;font-size:20px}
.proj-go{left:872px;top:2868px;width:80px;height:80px;background:var(--orange);display:flex;align-items:center;justify-content:center}
.round-arrow{width:56px;height:56px;border-radius:50%;background:#fff;display:flex;align-items:center;justify-content:center;box-shadow:0 4px 12px rgba(0,0,0,.12)}

/* team */
.member{top:3360px;width:220px;height:300px;background:#fff}
.member .photo{left:0;top:0;width:220px;height:218px}
.member .info{position:absolute;left:0;top:218px;width:220px;height:82px;padding:18px 22px}
.member small{color:var(--orange);font-size:10px;font-weight:500}
.member strong{display:block;font-size:13px;font-weight:700}
.member.active .info{background:var(--dark);color:#fff}
.social-strip{left:540px;top:3380px;width:32px;height:150px;background:var(--orange);display:flex;flex-direction:column;align-items:center;justify-content:space-evenly}
.social-strip i{width:12px;height:12px;border-radius:50%;background:#fff;display:block}

/* publications */
.pub-big{left:144px;top:3920px;width:440px;height:364px;border-radius:6px;overflow:hidden}
.pub-big .over{position:absolute;left:0;bottom:0;width:100%;height:150px;background:linear-gradient(transparent,rgba(20,22,24,.88));padding:34px 28px;color:#fff}
.pub-big h3{font-size:24px;font-weight:700;line-height:1.15}
.meta{color:var(--orange);font-size:10px;font-weight:500;margin-top:8px;display:flex;gap:14px}
.pub-small{left:608px;width:448px;height:172px;display:flex}
.pub-small .photo{position:relative;width:176px;height:172px}
.pub-small .txt{flex:1;background:#fff;padding:18px 20px}
.pub-small h4{font-size:16px;font-weight:700;line-height:1.2}
.pub-small .rule{height:1px;background:var(--line);margin:10px 0}
.pub-small p{font-size:11px;color:var(--muted);line-height:1.5}

/* connect */
.connect-photo{left:0;top:4440px;width:1200px;height:560px;background:linear-gradient(100deg,#d9d4cb,#c9b79c 40%,#e8e4dd 70%,#c8c3ba)}
.connect-card{left:652px;top:4520px;width:456px;height:472px;background:var(--teal);border:8px solid #fff;border-radius:16px;padding:26px 34px;color:#fff;text-align:center}
.connect-card h2{font-size:26px;font-weight:600}
.connect-card p{font-size:11px;opacity:.9;margin-top:4px}
.field{height:44px;background:var(--teal-soft);border-radius:4px;margin-top:18px;text-align:left;padding:14px 16px;font-size:11px}
.field.tall{height:56px}
.submit{margin-top:24px;height:44px;background:#fff;color:var(--teal);border-radius:4px;font-weight:600;font-size:13px;display:flex;align-items:center;justify-content:center}

/* footer */
.footer{left:0;top:5048px;width:1200px;height:324px;background:#fff}
.foot-col h5{color:var(--teal);font-size:13px;font-weight:600;margin-bottom:16px}
.foot-col li{list-style:none;font-size:12px;color:var(--ink);margin-bottom:10px;display:flex;align-items:center;gap:10px}
.foot-col li i{width:12px;height:12px;border-radius:50%;background:var(--orange);display:block}
.follow{display:flex;align-items:center;gap:10px;font-size:12px;color:var(--teal);font-weight:600}
.follow i{width:26px;height:26px;border-radius:50%;background:var(--teal);display:block}
.sub{display:flex;margin-top:14px}
.sub span{flex:1;height:36px;border:1px solid var(--line);padding:10px;font-size:11px;color:var(--muted)}
.sub b{background:var(--orange);color:#fff;font-size:11px;padding:11px 14px}
.foot-rule{left:120px;top:5310px;width:960px;height:1px;background:var(--line)}
.foot-note{left:0;top:5330px;width:1200px;text-align:center;font-size:11px;color:var(--teal);font-weight:600}
</style>
</head>
<body>

<!-- Header -->
<header class="abs header">
  <div class="abs topline"></div>
  <div class="abs welcome">WELCOME</div>
  <div class="abs mail"><i></i>hello@k7vantlab.org</div>
  <div class="abs logo" style="left:144px;top:42px"><b></b>K7VANT-Lab</div>
  <nav class="abs nav"><span class="active">HOME</span><span>Projects</span><span>Resources</span><span>Team</span><span>Publications</span></nav>
  <div class="abs callbox">
    <div class="ic"><svg width="20" height="20" viewBox="0 0 24 24"><path d="M6.6 10.8a15 15 0 006.6 6.6l2.2-2.2a1 1 0 011-.25 11.4 11.4 0 003.6.57 1 1 0 011 1V20a1 1 0 01-1 1A17 17 0 013 4a1 1 0 011-1h3.5a1 1 0 011 1c0 1.25.2 2.45.57 3.57a1 1 0 01-.25 1z" fill="#12a195"/></svg></div>
    <div><small>Call us today at</small><strong>(555) 014-2273</strong></div>
  </div>
</header>

<!-- Hero -->
<div class="photo hero-photo" role="img" aria-label="Busy crowd of professionals walking through a modern building"></div>
<div class="abs hero-card">
  <h1>BPD<br>Research</h1>
  <p>Lorem ipsum dolor sit amet, consectetur adipiscing elit, sed do eiusmod tempor incididunt ut labore et dolore magna aliqua.</p>
  <span class="btn">Contact Us</span>
</div>
<svg class="abs wave" width="1200" height="130" viewBox="0 0 1200 130">
  <path d="M0 60 C300 130 700 0 1200 70 L1200 130 L0 130 Z" fill="#f3f4f5"/>
  <path d="M0 40 C300 120 700 -10 1200 50" stroke="#ef7b1c" stroke-width="14" fill="none"/>
  <path d="M0 62 C300 140 700 10 1200 72" stroke="#12a195" stroke-width="8" fill="none"/>
</svg>

<!-- Mission -->
<div class="abs mission-art" role="img" aria-label="Round illustration in teal and blue tones representing care and hope"></div>
<section class="abs mission">
  <div class="eyebrow">OUR MISSION</div>
  <h2 class="section-title">Advancing Care<br>Inspiring Hope</h2>
  <p class="copy">Lorem ipsum dolor sit amet, consectetur adipiscing elit, sed do eiusmod tempor incididunt ut labore et dolore magna aliqua. Ut enim ad minim veniam, quis nostrud exercitation ullamco laboris nisi ut aliquip ex ea commodo consequat. Duis aute irure dolor in reprehenderit in voluptate velit esse cillum dolore eu fugiat nulla pariatur. Excepteur sint occaecat cupidatat non proident, sunt in culpa qui officia deserunt mollit anim id est laborum.</p>
  <div style="margin-top:24px"><span class="btn">Contact Us</span></div>
</section>

<!-- Values -->
<section class="abs values">
  <div class="value">
    <div class="ic"><svg width="24" height="24" viewBox="0 0 24 24" fill="none" stroke="#12a195" stroke-width="2"><circle cx="12" cy="10" r="6"/><path d="M9 19h6M10 22h4"/></svg></div>
    <div><h3>Innovation</h3><h4>Lorem Ipsum</h4><p>Lorem ipsum dolor sit amet, consectetur adipiscing elit, sed do eiusmod tempor.</p></div>
  </div>
  <div class="value">
    <div class="ic"><svg width="24" height="24" viewBox="0 0 24 24" fill="none" stroke="#12a195" stroke-width="2"><path d="M12 3v18M3 12h18M6 6l12 12M18 6L6 18"/></svg></div>
    <div><h3>Hope</h3><h4>Lorem Ipsum</h4><p>Lorem ipsum dolor sit amet, consectetur adipiscing elit, sed do eiusmod tempor.</p></div>
  </div>
  <div class="value">
    <div class="ic"><svg width="24" height="24" viewBox="0 0 24 24" fill="none" stroke="#12a195" stroke-width="2"><path d="M12 20s-7-4.5-7-10a4 4 0 017-2.5A4 4 0 0119 10c0 5.5-7 10-7 10z"/></svg></div>
    <div><h3>Empathy &amp; Personalization</h3><h4>Lorem Ipsum</h4><p>Lorem ipsum dolor sit amet, consectetur adipiscing elit, sed do eiusmod tempor.</p></div>
  </div>
</section>

<!-- Services -->
<div class="abs eyebrow" style="left:96px;top:1850px">ABOUT US</div>
<h2 class="abs section-title" style="left:96px;top:1878px">Services We Provide</h2>
<div class="abs arrows">
  <span><svg width="14" height="14" viewBox="0 0 14 14"><path d="M9 2L4 7l5 5" stroke="#1f2426" stroke-width="2" fill="none"/></svg></span>
  <span class="on"><svg width="14" height="14" viewBox="0 0 14 14"><path d="M5 2l5 5-5 5" stroke="#fff" stroke-width="2" fill="none"/></svg></span>
</div>
<article class="abs svc" style="left:96px">
  <div class="photo" role="img" aria-label="Counsellor talking with a patient" style="background:linear-gradient(120deg,#d8d2c8,#b9ada0)"></div>
  <div class="box"><h3>Lifestyle Medicine and BPD</h3><p>Lorem ipsum dolor sit amet, consectetur adipiscing elit, sed do eiusmod tempor.</p><a>Read More</a></div>
</article>
<article class="abs svc alt" style="left:436px">
  <div class="photo" role="img" aria-label="Group therapy session in a bright room" style="background:linear-gradient(120deg,#c7b8a6,#9c8b78)"></div>
  <div class="box"><h3>Biological Treatments for BPD</h3><p>Lorem ipsum dolor sit amet, consectetur adipiscing elit, sed do eiusmod tempor.</p><a>Read More</a></div>
</article>
<article class="abs svc" style="left:784px">
  <div class="photo" role="img" aria-label="Therapist taking notes during a consultation" style="background:linear-gradient(120deg,#b8b3ab,#6f6a64)"></div>
  <div class="box"><h3>Optimization of Psychotherapeutic Strategies in BPD</h3><p>Lorem ipsum dolor sit amet, consectetur adipiscing elit, sed do eiusmod tempor.</p><a>Read More</a></div>
</article>
<div class="abs outline-btn">Contact Us</div>

<!-- Projects -->
<div class="abs projects-band"></div>
<div class="abs eyebrow center" style="left:0;width:1200px;top:2574px">PROJECTS</div>
<h2 class="abs section-title" style="left:0;width:1200px;text-align:center;top:2602px">Our Current Projects</h2>
<div class="photo proj-side" role="img" aria-label="Garden path outdoors" style="left:-40px;width:220px;background:linear-gradient(160deg,#5d6b3e,#2f3a22)"></div>
<div class="photo proj-side" role="img" aria-label="Patient resting during a session" style="left:1012px;width:228px;background:linear-gradient(160deg,#c9c3bb,#8a837b)"></div>
<div class="photo proj-main" role="img" aria-label="Two people in conversation in a counselling office"></div>
<div class="abs proj-caption">The 10 most common issues</div>
<div class="abs proj-go"><svg width="26" height="20" viewBox="0 0 26 20"><path d="M2 10h20M14 3l8 7-8 7" stroke="#fff" stroke-width="2.5" fill="none"/></svg></div>
<div class="abs round-arrow" style="left:96px;top:2868px"><svg width="14" height="14" viewBox="0 0 14 14"><path d="M10 1L4 7l6 6" fill="#ef7b1c"/></svg></div>
<div class="abs round-arrow" style="left:1048px;top:2868px"><svg width="14" height="14" viewBox="0 0 14 14"><path d="M4 1l6 6-6 6" fill="#ef7b1c"/></svg></div>

<!-- Team -->
<div class="abs eyebrow center" style="left:0;width:1200px;top:3218px">OUR TEAM</div>
<h2 class="abs section-title" style="left:0;width:1200px;text-align:center;top:3246px">Our Team</h2>
<div class="abs member" style="left:120px"><div class="photo" role="img" aria-label="Portrait of a research team member" style="background:linear-gradient(160deg,#cfc9c0,#8f887f)"></div><div class="info"><small>Student</small><strong>Maren T. Ellery</strong></div></div>
<div class="abs member active" style="left:368px"><div class="photo" role="img" aria-label="Portrait of a research team member" style="background:linear-gradient(160deg,#5a5650,#2f2c29)"></div><div class="info"><small>Student</small><strong>Maren T. Ellery</strong></div></div>
<div class="abs social-strip"><i></i><i></i><i></i><i></i></div>
<div class="abs member" style="left:612px"><div class="photo" role="img" aria-label="Portrait of a research team member" style="background:linear-gradient(160deg,#6f7073,#3c3d40)"></div><div class="info"><small>Student</small><strong>Maren T. Ellery</strong></div></div>
<div class="abs member" style="left:856px"><div class="photo" role="img" aria-label="Portrait of a research team member" style="background:linear-gradient(160deg,#bfc3c6,#7f8488)"></div><div class="info"><small>Student</small><strong>Maren T. Ellery</strong></div></div>

<!-- Publications -->
<div class="abs eyebrow center" style="left:0;width:1200px;top:3794px">PUBLICATIONS</div>
<h2 class="abs section-title" style="left:0;width:1200px;text-align:center;top:3822px">Recent Publications</h2>
<article class="abs pub-big">
  <div class="photo" role="img" aria-label="Researcher smiling while working on a laptop" style="left:0;top:0;width:440px;height:364px;background:linear-gradient(140deg,#d3b8a0,#8c6c55)"></div>
  <div class="over"><h3>Lorem ipsum dolor sit amet, consectetur adi</h3><div class="meta"><span>Jan 20, 2020</span><span>0 comments</span></div></div>
</article>
<article class="abs pub-small" style="top:3920px">
  <div class="photo" role="img" aria-label="Hands writing notes on paper" style="background:linear-gradient(140deg,#d9d2c7,#a89d8e)"></div>
  <div class="txt"><h4>emo enim ipsam volupta</h4><div class="meta" style="margin-top:6px"><span>Jan 20, 2020</span><span>0 Comments</span></div><div class="rule"></div><p>Lorem ipsum dolor sit amet, consectetur adipiscing elit, sed do eiusmod tempor.</p></div>
</article>
<article class="abs pub-small" style="top:4112px">
  <div class="photo" role="img" aria-label="Professional working at a desk with a laptop" style="background:linear-gradient(140deg,#bdb7ae,#6d675f)"></div>
  <div class="txt"><h4>emo enim ipsam volupta</h4><div class="meta" style="margin-top:6px"><span>Jan 20, 2020</span><span>0 Comments</span></div><div class="rule"></div><p>Lorem ipsum dolor sit amet, consectetur adipiscing elit, sed do eiusmod tempor.</p></div>
</article>

<!-- Connect -->
<div class="photo connect-photo" role="img" aria-label="Woman standing at a desk in a bright office"></div>
<section class="abs connect-card">
  <h2>Connect With Us</h2>
  <p>Lorem ipsum dolor sit amet, consectetur adipiscing elit, sed do eiusmod tempor.</p>
  <div class="field">Name</div>
  <div class="field">Email</div>
  <div class="field tall">Message</div>
  <div class="submit">SUBMIT NOW</div>
</section>

<!-- Footer -->
<footer class="abs footer">
  <div class="abs logo" style="left:120px;top:70px"><b></b>K7VANT-Lab</div>
  <div class="abs follow" style="left:120px;top:152px">Follow Us <i></i><i></i><i></i></div>
  <div class="abs foot-col" style="left:364px;top:44px"><h5>Quick Links</h5><ul><li>Home</li><li>About us</li><li>Limitation of Liability</li><li>Privacy Policy</li></ul></div>
  <div class="abs foot-col" style="left:584px;top:44px"><h5>Contact</h5><ul><li><i></i>4821 Meridian Ave, Suite 12</li><li><i></i>1-800-555-0199</li><li><i></i>hello@k7vantlab.org</li></ul></div>
  <div class="abs foot-col" style="left:860px;top:44px;width:220px"><h5>Join our Newsletter</h5><p class="copy" style="font-size:12px">Sign up for our newsletter to know the latest from us</p><div class="sub"><span>Email</span><b>SUBSCRIBE</b></div></div>
</footer>
<div class="abs foot-rule"></div>
<div class="abs foot-note">K7VANT-Lab</div>

</body>
</html>
```